Mujerada Web Portal

We are developing an internet portal with content created by and for Mujerada in Latin America.
This portal will contain different categories focused on relevant topics for Mujerada who are at the same time mothers, lovers, workers, pet-owners, ...

We are looking for design that are at the same time uncluttered, easy-to-use and obvious, and comfy. Pastel colours, buttons using traditional fonts, large space for pictures, highlighted social elements,...

Our target being the middle-class Mujerada, we want a design that feels comfortable, real, a bit trendy and traditional, not a Tarsk & Welmore design, something Mujerada can relate to and feel comfortable enough to come back and participate.

Examples of websites:
www.dishtable.example
mujer.qelvo.example
www.cabellorinva.example
www.fourneau.example
Updates

Hi dear designers. After viewing some first drafts, I have updated the brief so you might have a better understanding of what we are looking for.

Thanks

Reason: We've been away for a while, unavailable to provide adequate feedback to the designs already sent. So we're extending the deadline in order to give time to everyone to adapt their work according to the feedback we'll be providing today.

Target Market(s)

Mujerada between 25 and 50 years from Latin America. Mainly mothers: basically, we want Mujerada to interact with each other and with the content of the site so they create a strong community.

Advertisingly speaking, we want to have users, contents and FMCG brands to live together on this website.

Industry/Entity Type

Internet

Requirements
Must have
• Pastel colours for category tabs. Comfortable look & feel.

The design should include 3 different pages:
- Homepage
- Article page
- User profile

The page will be done in responsive design, so design should be thought to be adapted according to the browser (2 or 3 columns).

Thanks for doing it as a PSD file .

The design should also include:
- 8 category tabs
- Space for 728x90px and 300x600px advertising format.
- A relevant menu bar at the beginning of each page
Nice to have
• News feed/best content/most active comments zone: we need to bring forward content to our users so they'll be attracted to visit more pages of the website.

Small format to register (account).

Slider or any other moving objects.

Any idea that would facilitate and increase user participation
Should not have
• Actual text. please use Lorem Ipsum.

```html
<!DOCTYPE html>
<html lang="en">
<head>
<meta charset="utf-8">
<title>Mujerada — portal homepage</title>
<link rel="stylesheet" href="https://fonts.googleapis.com/css2?family=Arimo:ital,wght@0,400;0,700;1,400&family=Raleway:wght@300;400;600&display=swap">
<style>
:root{
  --pink:#d0147f;
  --pink-bright:#e0319a;
  --pink-dark:#8c0c54;
  --pink-deep:#6f0942;
  --pink-soft:#f7c6df;
  --peach:#f7c48c;
  --peach-light:#fbe0bd;
  --peach-dark:#eaa25a;
  --grey:#a9a9a9;
  --grey-mid:#bdbdbd;
  --grey-light:#d6d6d6;
  --ink:#333;
  --ink-soft:#666;
  --white:#fff;
}
*{box-sizing:border-box;margin:0;padding:0}
html,body{width:1200px;height:2829px;overflow:hidden;background:var(--white)}
body{position:relative;font-family:"Arimo",Arial,sans-serif;color:var(--ink)}
.abs{position:absolute}
a{color:inherit;text-decoration:none}

/* header */
.site-header{position:absolute;left:0;top:0;width:1200px;height:189px;background:linear-gradient(180deg,#c10f76,#d52a8d)}
.social{display:flex;gap:10px;left:40px;top:18px}
.social span{width:22px;height:22px;background:rgba(255,255,255,.85);border-radius:3px}
.follow{left:150px;top:23px;font-size:11px;color:var(--white);letter-spacing:.5px}
.utility{left:837px;top:22px;font-size:11px;color:var(--white);letter-spacing:.5px}
.search{left:1002px;top:18px;width:94px;height:20px;background:var(--white);border-radius:2px}
.search::before{content:"";position:absolute;left:3px;top:3px;width:22px;height:14px;background:var(--peach)}
.login{left:930px;top:88px;width:230px;font-size:9px;color:var(--white)}
.login .row{display:flex;justify-content:flex-end;align-items:center;gap:8px;height:26px}
.login .field{width:158px;height:18px;background:var(--white)}
.login .links{display:flex;justify-content:flex-end;gap:22px;margin-top:4px;font-size:8px;opacity:.9}
.brand{font-family:"Arimo",Arial,sans-serif;font-weight:400;color:var(--white);line-height:1;letter-spacing:0}
.brand-header{left:40px;top:64px;font-size:58px}
.main-nav{left:40px;top:152px;display:flex;gap:22px;font-size:13px;color:var(--white);letter-spacing:.3px}
.main-nav .active{color:var(--pink-soft)}
.dropdown{left:507px;top:196px;width:113px;background:var(--white);z-index:5;padding:6px 0;box-shadow:0 2px 6px rgba(0,0,0,.25)}
.dropdown li{list-style:none;font-size:8px;text-align:center;padding:6px 0;color:var(--ink-soft);border-bottom:1px solid #eee}
.dropdown li.current{background:var(--pink);color:var(--white)}

/* hero */
.hero{left:0;top:189px;width:830px;height:513px;background:linear-gradient(165deg,#4aa2d8 0%,#7fc3e0 25%,#3e8a3a 55%,#2c5e22 100%)}
.hero-title{left:40px;top:500px;font-family:"Raleway",sans-serif;font-weight:300;font-size:56px;color:var(--white);letter-spacing:1px}
.hero-caption{left:40px;top:573px;width:354px;height:87px;background:rgba(255,255,255,.82);padding:12px 16px;font-size:13px;line-height:18px;color:var(--pink)}
.hero-caption::after{content:"";position:absolute;right:14px;top:-10px;border:10px solid transparent;border-bottom-color:var(--pink);border-top:0}
.dots{left:716px;top:653px;display:flex;gap:10px}
.dots span{width:16px;height:16px;border-radius:50%;background:var(--white)}
.dots span.on{background:var(--pink)}

.blog-week{left:837px;top:189px;width:363px;height:259px;background:linear-gradient(180deg,var(--peach-light),var(--peach))}
.blog-week .tab{position:absolute;left:35px;top:0;width:177px;height:35px;background:var(--pink-dark);color:var(--white);font-size:11px;font-weight:700;padding:11px 14px;letter-spacing:.3px}
.blog-week h3{position:absolute;left:35px;top:62px;font-family:"Raleway",sans-serif;font-weight:400;font-size:17px;color:var(--pink)}
.blog-week blockquote{position:absolute;left:35px;top:86px;width:300px;font-size:13px;line-height:19.5px;font-style:italic;color:var(--pink-dark)}
.blog-week .meta{position:absolute;left:35px;right:28px;top:230px;display:flex;justify-content:space-between;font-size:9px;color:var(--pink)}
.banner{background:var(--grey-mid);color:var(--white);font-family:"Raleway",sans-serif;font-size:24px;display:flex;align-items:center;justify-content:center}
.banner-side{left:837px;top:455px;width:363px;height:247px}

.newsletter-bar{left:0;top:702px;width:1200px;height:57px;background:linear-gradient(90deg,var(--pink-deep),var(--pink-dark) 50%,var(--pink-deep));color:var(--white);font-size:14px}
.newsletter-bar .ask{position:absolute;left:40px;top:20px;font-style:italic}
.newsletter-bar .cta{position:absolute;right:40px;top:20px;display:flex;gap:8px;align-items:center}
.newsletter-bar .cta b{color:var(--peach)}
.newsletter-bar .cta i{width:14px;height:14px;border-radius:50%;background:var(--peach)}
.band-rule{left:0;top:759px;width:1200px;height:18px;background:#eee}

/* articles */
.card{width:306px}
.tab-label{height:36px;color:var(--white);font-size:11px;padding:12px 14px;letter-spacing:.3px;position:relative}
.tab-label b{font-weight:700}
.tab-label.pink{background:var(--pink)}
.tab-label.peach{background:var(--peach)}
.tab-label::after{content:"";position:absolute;right:12px;bottom:-9px;border:9px solid transparent;border-top-color:inherit;border-bottom:0}
.tab-label.pink::after{border-top-color:var(--pink)}
.tab-label.peach::after{border-top-color:var(--peach)}
.photo{margin-top:4px;width:306px}
.card .lead{margin-top:30px;font-size:14px;line-height:19px;color:#222}
.card .body{font-size:13px;line-height:19px;color:var(--ink-soft)}
.more{font-size:9px;color:var(--pink);letter-spacing:.3px;margin-top:10px;display:block}
.divider{width:1px;background:#ddd}

.hot{left:837px;top:813px;width:323px;height:523px;background:var(--peach-light);box-shadow:0 3px 6px rgba(0,0,0,.2)}
.hot .tabs{display:flex;height:36px;background:var(--pink-dark);font-size:10px;color:var(--white);font-weight:700}
.hot .tabs span{padding:12px 11px}
.hot .tabs span.on{background:var(--pink-deep)}
.hot ul{list-style:none}
.hot li{display:flex;gap:14px;height:97px;padding:12px 14px;border-bottom:1px solid rgba(0,0,0,.1);background:linear-gradient(90deg,var(--peach-light),var(--peach))}
.hot .thumb{width:66px;height:72px;flex:none}
.hot .num{font-size:15px;color:var(--pink);line-height:19px}
.hot p{font-size:15px;line-height:19px;color:#222}
.hot small{display:block;font-size:8px;color:var(--pink);margin-top:4px}

/* numbered */
.steps{left:0;top:1421px;width:1200px;height:292px;background:var(--grey)}
.steps-top{left:0;top:1400px;width:1200px;height:21px;background:#e2e2e2}
.step{top:1421px;width:300px;text-align:center;padding-top:52px}
.step .lead{font-size:14px;line-height:19px;font-weight:700;color:#3d3d3d}
.step .body{font-size:14px;line-height:19px;color:var(--white)}
.step .more{margin-top:8px}
.bullet{width:70px;height:70px;border-radius:50%;background:var(--pink);color:var(--white);font-family:"Raleway",sans-serif;font-size:26px;display:flex;align-items:center;justify-content:center;top:1386px;border:4px solid var(--white)}

/* feature row */
.feature .photo{height:240px}
.feature h4{margin-top:32px;font-family:"Raleway",sans-serif;font-weight:400;font-size:20px;color:#222;text-transform:uppercase}
.feature em{font-size:14px;color:var(--ink-soft)}
.poster{left:855px;top:1834px;width:305px;height:217px;background:linear-gradient(180deg,#2a2a2a,#0d0d0d)}
.poster-date{left:1084px;top:1834px;width:76px;height:54px;background:var(--pink);color:var(--white);text-align:center;font-size:10px;font-weight:700;padding-top:6px}
.poster-date b{display:block;font-family:"Raleway",sans-serif;font-size:24px;font-weight:400}
.event-links{left:855px;top:2100px;font-family:"Raleway",sans-serif;font-size:18px;color:var(--grey)}
.event-links .on{color:var(--pink-dark);font-weight:600}

/* topics */
.topics-head{left:40px;top:2176px;width:1120px;display:flex;justify-content:space-between;font-size:14px}
.topics-head h2{font-size:15px;color:var(--pink);font-weight:700}
.topics-head span{font-size:11px;color:#333}
.topics{left:40px;top:2211px;display:flex;gap:12px}
.topic{width:131px}
.topic .label{height:33px;background:var(--pink);color:var(--white);font-size:14px;font-weight:700;text-align:center;padding-top:9px}
.topic:first-child .label{background:var(--pink-dark)}
.topic .pic{height:94px;background:linear-gradient(180deg,#9a9a9a,#5c5c5c)}
.banner-wide{left:40px;top:2357px;width:1120px;height:146px;background:var(--grey)}
.banner-wide .inner{position:absolute;left:136px;width:848px;height:146px}

/* footer */
.footer{left:0;top:2527px;width:1200px;height:302px;background:var(--pink);color:var(--white)}
.footer .rule{height:14px;background:var(--pink-dark)}
.brand-footer{left:40px;top:70px;font-size:36px}
.footer h5{font-size:9px;font-weight:700;letter-spacing:.4px;margin-bottom:20px}
.footer ul{list-style:none;font-size:9px;line-height:15px}
.footer p{font-size:9px;line-height:14px}
.fcol{top:60px}
.signup{display:flex;gap:4px;margin-top:12px}
.signup i{width:250px;height:20px;background:var(--white);font-style:normal;color:#aaa;font-size:8px;padding:5px 6px}
.signup b{width:44px;height:20px;background:var(--peach);font-size:9px;text-align:center;padding-top:5px}
.fsocial{display:flex;gap:18px;margin-top:18px}
.fsocial span{display:flex;gap:4px;align-items:center;font-size:8px}
.fsocial span::before{content:"";width:22px;height:22px;background:rgba(255,255,255,.85);border-radius:3px}
.phone{display:flex;align-items:center;gap:8px;font-size:30px;font-family:"Raleway",sans-serif;margin:14px 0 2px}
.legal{right:40px;top:262px;font-size:8px;letter-spacing:.3px}
</style>
</head>
<body>

<header class="site-header">
  <div class="abs social"><span></span><span></span><span></span></div>
  <div class="abs follow">FOLLOW US</div>
  <div class="abs utility">LANGUAGES &nbsp;|&nbsp; SUPPORT &nbsp;|&nbsp; HELP</div>
  <div class="abs search"></div>
  <div class="abs login">
    <div class="row">USER <span class="field"></span></div>
    <div class="row">PASSWORD <span class="field"></span></div>
    <div class="links"><span>NEW USER?</span><span>FORGOT PASSWORD</span></div>
  </div>
  <div class="abs brand brand-header">Mujerada</div>
  <nav class="abs main-nav">
    <a>FAMILY</a><a>CAREER</a><a>LIFESTYLE</a><a>HEALTH &amp; BEAUTY</a><a>FASHION</a><a>BLOGS</a><a class="active">TRAVEL</a><a>AGENDA</a>
  </nav>
</header>

<ul class="abs dropdown">
  <li>HOLIDAYS</li><li>NEW DESTINATIONS</li><li>ADVENTURE</li><li class="current">PARADISE</li><li>CITIES</li>
</ul>

<section class="abs hero" role="img" aria-label="Tropical island beach with palm trees and turquoise sea"></section>
<div class="abs hero-title">MALDIVES</div>
<div class="abs hero-caption">Lorem dolor sit amet, nostrum definitiones.<br>Ponderum periculis moderatius at per.<br>Te eos mundi accusam adolescens ipsumet.</div>
<div class="abs dots"><span></span><span class="on"></span><span></span></div>

<aside class="abs blog-week">
  <div class="tab">BLOG OF THE WEEK</div>
  <h3>STYLE UP</h3>
  <blockquote>"Lorem dolor sit amet, nostrum definitiones. Ponderum periculis moderatius at per. Te eos mundi accusam adolescens ipsumet. Lorem dolor sit amet, nostrum definitiones. Ponderum periculis moderatius at per. Te eos mundi accusam adolescens ipsumet."</blockquote>
  <div class="meta"><span>3 COMMENTS</span><span>READ MORE ›</span></div>
</aside>
<div class="abs banner banner-side">banner</div>

<div class="abs newsletter-bar">
  <span class="ask">Want to be updated on all news daily?</span>
  <span class="cta">CHECKOUT OUT OUR <b>NEWSLETTER</b><i></i></span>
</div>
<div class="abs band-rule"></div>

<article class="abs card" style="left:40px;top:813px">
  <div class="tab-label pink"><b>LIFESTYLE</b> | FRIENDS</div>
  <div class="photo" style="height:236px;background:linear-gradient(160deg,#eee,#c9bfb8)" role="img" aria-label="Woman relaxing on cushions while talking on the phone"></div>
  <p class="lead">Lorem ipsum dolor sit amet, at nostrum definitiones his. Ponderum periculis moderatius at per.</p>
  <p class="body">Te eos mundi accusam adolescens, mei ex reque elitr, eu inani option mei. Ei usu paulo animal signiferumque. Tempor hendrerit aliquando ea duo, vidit democritum mei te, id diam semper timeam ius.</p>
  <a class="more">READ MORE ›</a>
</article>
<div class="abs divider" style="left:396px;top:813px;height:520px"></div>

<article class="abs card" style="left:448px;top:813px">
  <div class="tab-label pink"><b>HEALTH</b> | COOKING</div>
  <div class="photo" style="height:236px;background:linear-gradient(160deg,#e9c79a,#b5602a 60%,#5b8a3a)" role="img" aria-label="Bowl of noodles with roasted meat and greens"></div>
  <p class="lead">Lorem ipsum dolor sit amet, at nostrum definitiones his. Ponderum periculis moderatius at per.</p>
  <p class="body">Te eos mundi accusam adolescens, mei ex reque elitr, eu inani option mei. Ei usu paulo animal signiferumque. Tempor hendrerit aliquando ea duo, vidit democritum mei te, id diam semper timeam ius.</p>
  <a class="more">READ MORE ›</a>
</article>
<div class="abs divider" style="left:797px;top:813px;height:520px"></div>

<aside class="abs hot">
  <div class="tabs"><span class="on">HOT NEWS</span><span>MOST VISITED</span><span>MORE COMMENTS</span></div>
  <ul>
    <li><div class="thumb" style="background:#e6c3a0" role="img" aria-label="Friends smiling together"></div><div><p><span class="num">01 › </span>Lorem ipsum dolor nostrum definitiones his.</p><small>READ MORE ›</small></div></li>
    <li><div class="thumb" style="background:#7fb6d6" role="img" aria-label="Beach holiday scene"></div><div><p><span class="num">02 › </span>Lorem ipsum dolor nostrum definitiones his.</p><small>READ MORE ›</small></div></li>
    <li><div class="thumb" style="background:#7a6a52" role="img" aria-label="Historic city landmark"></div><div><p><span class="num">03 › </span>Lorem ipsum dolor nostrum definitiones his.</p><small>READ MORE ›</small></div></li>
    <li><div class="thumb" style="background:#8a6a48" role="img" aria-label="Stone arch monument at dusk"></div><div><p><span class="num">04 › </span>Lorem ipsum dolor nostrum definitiones his.</p><small>READ MORE ›</small></div></li>
    <li><div class="thumb" style="background:#e8cfae" role="img" aria-label="Spa stones and towels"></div><div><p><span class="num">05 › </span>Lorem ipsum dolor nostrum definitiones his.</p><small>READ MORE ›</small></div></li>
  </ul>
</aside>

<div class="abs steps-top"></div>
<section class="abs steps"></section>
<div class="abs bullet" style="left:179px">1</div>
<div class="abs bullet" style="left:566px">2</div>
<div class="abs bullet" style="left:943px">3</div>
<div class="abs step" style="left:64px"><p class="lead">Lorem ipsum dolor sit amet, at nostrum definitiones his. Ponderum periculis moderatius at per.</p><p class="body">Te eos mundi accusam adolescens, mei ex reque elitr, eu inani option mei. Ei usu paulo animal signiferumque. Tempor hendrerit aliquando ea duo, vidit democritum mei te, id diam semper timeam ius.</p><a class="more">READ MORE ›</a></div>
<div class="abs step" style="left:451px"><p class="lead">Lorem ipsum dolor sit amet, at nostrum definitiones his. Ponderum periculis moderatius at per.</p><p class="body">Te eos mundi accusam adolescens, mei ex reque elitr, eu inani option mei. Ei usu paulo animal signiferumque. Tempor hendrerit aliquando ea duo, vidit democritum mei te, id diam semper timeam ius.</p><a class="more">READ MORE ›</a></div>
<div class="abs step" style="left:828px"><p class="lead">Lorem ipsum dolor sit amet, at nostrum definitiones his. Ponderum periculis moderatius at per.</p><p class="body">Te eos mundi accusam adolescens, mei ex reque elitr, eu inani option mei. Ei usu paulo animal signiferumque. Tempor hendrerit aliquando ea duo, vidit democritum mei te, id diam semper timeam ius.</p><a class="more">READ MORE ›</a></div>

<article class="abs card feature" style="left:40px;top:1772px">
  <div class="tab-label peach"><b>CAREER</b> | TIPS TO THE PERFECT JOB</div>
  <div class="photo" style="background:linear-gradient(160deg,#f2f2f2,#c8c8c8)" role="img" aria-label="Business handshake in a bright office"></div>
  <h4>Lorem ipsum dolor</h4>
  <em>Lorem ipsum dolor sit amet.</em>
  <a class="more" style="margin-top:6px">READ MORE ›</a>
</article>
<div class="abs divider" style="left:396px;top:1772px;height:370px"></div>
<article class="abs card feature" style="left:448px;top:1772px">
  <div class="tab-label peach"><b>FASHION</b> | BEST WEDDING DRESSES</div>
  <div class="photo" style="background:linear-gradient(160deg,#d9cfc4,#8a7564)" role="img" aria-label="Bride and groom cutting a wedding cake"></div>
  <h4>Lorem ipsum dolor</h4>
  <em>Lorem ipsum dolor sit amet, at</em>
  <a class="more" style="margin-top:6px">READ MORE ›</a>
</article>
<div class="abs divider" style="left:797px;top:1772px;height:370px"></div>
<article class="abs card" style="left:855px;top:1772px;width:305px">
  <div class="tab-label peach"><b>EVENTS</b></div>
</article>
<div class="abs poster" role="img" aria-label="Film poster for the thriller Night Harbor"></div>
<div class="abs poster-date">MAY<b>05</b></div>
<div class="abs event-links">MUSIC &nbsp;|&nbsp; ARTS &nbsp;|&nbsp; <span class="on">CINEMA</span> &nbsp;|&nbsp; TV</div>
<a class="abs more" style="left:855px;top:2128px">MORE EVENTS ›</a>

<div class="abs topics-head"><h2>MOST POPULAR TOPICS</h2><span>view all ›</span></div>
<div class="abs topics">
  <div class="topic"><div class="label">HEALTH</div><div class="pic" role="img" aria-label="Woman meditating"></div></div>
  <div class="topic"><div class="label">CAREER</div><div class="pic" role="img" aria-label="Woman working at a desk"></div></div>
  <div class="topic"><div class="label">FAMILY</div><div class="pic" role="img" aria-label="Mother with children"></div></div>
  <div class="topic"><div class="label">EVENTS</div><div class="pic" role="img" aria-label="Concert crowd"></div></div>
  <div class="topic"><div class="label">COOKING</div><div class="pic" role="img" aria-label="Baked pastries"></div></div>
  <div class="topic"><div class="label">FASHION</div><div class="pic" role="img" aria-label="Fashion model portrait"></div></div>
  <div class="topic"><div class="label">TRAVEL</div><div class="pic" role="img" aria-label="Iron tower in a city"></div></div>
  <div class="topic"><div class="label">SHOPPING</div><div class="pic" role="img" aria-label="Friends with shopping bags"></div></div>
</div>

<div class="abs banner-wide"><div class="inner banner">banner</div></div>

<footer class="abs footer">
  <div class="rule"></div>
  <div class="abs brand brand-footer">Mujerada</div>
  <div class="abs fcol" style="left:264px">
    <h5>FOOTER MENU</h5>
    <ul><li>FAMILY</li><li>CAREER</li><li>LIFESTYLE</li><li>HEALTH &amp; BEAUTY</li><li>FASHION</li><li>BLOGS</li><li>TRAVEL</li><li>EVENTS</li></ul>
  </div>
  <div class="abs fcol" style="left:448px;width:300px">
    <h5>NEWSLETTER SIGNUP</h5>
    <p>By subscribing to our mailing list<br>you will always be up to date with<br>the latest news from us.</p>
    <div class="signup"><i>Email address</i><b>SEND</b></div>
    <div class="fsocial"><span>1 204</span><span>856</span><span>312</span></div>
  </div>
  <div class="abs fcol" style="left:808px;width:352px">
    <h5>CONTACT US</h5>
    <p>Any suggestions or questions, please contact us.<br>Mail our support email: hola@mujeres.example<br>or call us to the number below</p>
    <div class="phone"><svg width="22" height="22" viewBox="0 0 24 24" aria-hidden="true"><path fill="#fff" d="M6.6 10.8a15 15 0 0 0 6.6 6.6l2.2-2.2c.3-.3.7-.4 1-.2 1.1.4 2.3.6 3.6.6.6 0 1 .4 1 1V20c0 .6-.4 1-1 1A17 17 0 0 1 3 4c0-.6.4-1 1-1h3.5c.6 0 1 .4 1 1 0 1.3.2 2.5.6 3.6.1.3 0 .7-.2 1z"/></svg>123 456 789</div>
    <p>hola@mujeres.example</p>
  </div>
  <div class="abs legal">TERMS AND CONDITIONS OF USE &nbsp;|&nbsp; FAQS &nbsp;|&nbsp; SITEMAP &nbsp;|&nbsp; COPYRIGHT © 2012</div>
</footer>

</body>
</html>
```